Business Card Design

Business card design.

Business card is to have logo, website address and email address.

Website is www.brightkettle.ie
Email is info@brightkettle.ie
Logo uploaded

I have ordered Business Card Printing via Print Harbor, the Double-sided colour printed option with gloss finish.

Industry/Entity Type

Business

```html
<!DOCTYPE html>
<html lang="en">
<head>
<meta charset="utf-8">
<title>Bright Kettle – Business Card</title>
<link rel="stylesheet" href="https://fonts.googleapis.com/css2?family=Arimo:wght@700&display=swap">
<style>
  :root {
    --card-yellow: #fff200;
    --card-black: #0a0a0a;
    --placeholder-light: #ececec;
    --placeholder-dark: #cfcfcf;
    --backdrop: #e4e1dc;
    --text-black: #111111;
  }
  html, body {
    margin: 0;
    padding: 0;
    width: 1200px;
    height: 900px;
    overflow: hidden;
    background: var(--backdrop);
  }
  .sheet {
    position: relative;
    width: 1200px;
    height: 900px;
  }
  .card {
    position: absolute;
    left: 300px;
    width: 600px;
    height: 388px;
    background: var(--card-yellow);
    border-radius: 4px;
    overflow: hidden;
    box-shadow: 0 6px 18px rgba(0,0,0,0.18);
  }
  .card--back { top: 42px; }
  .card--front { top: 470px; }
  .card__shapes {
    position: absolute;
    inset: 0;
    width: 600px;
    height: 388px;
  }
  .brand-name {
    position: absolute;
    margin: 0;
    font-family: "Arimo", Arial, sans-serif;
    font-weight: 700;
    color: var(--text-black);
    letter-spacing: 0.5px;
    white-space: nowrap;
  }
  .card--back .brand-name {
    top: 40px;
    right: 28px;
    font-size: 31px;
  }
  .card--front .brand-name {
    left: 0;
    right: 0;
    bottom: 66px;
    text-align: center;
    font-size: 50px;
  }
  .contact {
    position: absolute;
    top: 170px;
    right: 30px;
    width: 320px;
    margin: 0;
    font-family: "Arimo", Arial, sans-serif;
    font-weight: 700;
    font-size: 25px;
    line-height: 1.4;
    color: var(--text-black);
    text-align: center;
  }
  .contact span { display: block; }
</style>
</head>
<body>
<main class="sheet">

  <section class="card card--back" aria-label="Card back: contact details">
    <svg class="card__shapes" viewBox="0 0 600 388">
      <defs>
        <linearGradient id="column-fill" x1="0" y1="0" x2="0" y2="1">
          <stop offset="0" stop-color="var(--placeholder-light)"/>
          <stop offset="1" stop-color="var(--placeholder-dark)"/>
        </linearGradient>
      </defs>
      <path class="side-band" d="M0 0 H150 C 255 120, 250 270, 95 388 H0 Z" fill="var(--card-black)"/>
      <rect class="illustration-area" x="58" y="38" width="96" height="314" rx="6"
            fill="url(#column-fill)" role="img"
            aria-label="Vertical column of emoticon illustrations"/>
    </svg>
    <h2 class="brand-name">BRIGHTKETTLE.IE</h2>
    <p class="contact">
      <span class="contact__web">www.brightkettle.ie</span>
      <span class="contact__email">info@brightkettle.ie</span>
    </p>
  </section>

  <section class="card card--front" aria-label="Card front: brand">
    <svg class="card__shapes" viewBox="0 0 600 388">
      <defs>
        <linearGradient id="row-fill" x1="0" y1="0" x2="1" y2="0">
          <stop offset="0" stop-color="var(--placeholder-light)"/>
          <stop offset="1" stop-color="var(--placeholder-dark)"/>
        </linearGradient>
      </defs>
      <path class="top-band" d="M0 0 H600 V70 C 470 190, 230 225, 0 195 Z" fill="var(--card-black)"/>
      <rect class="illustration-area" x="160" y="84" width="320" height="82" rx="6"
            fill="url(#row-fill)" role="img"
            aria-label="Horizontal row of emoticon illustrations"/>
    </svg>
    <h1 class="brand-name">BRIGHTKETTLE.IE</h1>
  </section>

</main>
</body>
</html>
```